Packaging Design for Vito Prime

We require an outstanding packaging design for our Vito Prime brand, which offers hydration electrolyte supplements specifically tailored for athletes and sporty individuals.

Benchmark packaging design from aquelle competitor attached. The product packaging contains 20 x 20g sticks of the product.

Target Market

Psychographic: Health-conscious, active lifestyle, values quality, functionality and sustainability.

product description 1:
HYDRATION BOOSTER
Refresh, Replenish, Recharge!

product description 2:
PREMIUM ISOTONIC ELECTROLYTE DRINK
Nutritional Expertise Since 1992.

Existing Logo: to add "since 1992"

Appeal to Target Market: Create a design that resonates with both men and women in the 25-55 age group.

Grafik Design: Develop a visually striking design that grabs attention in online retail environments like Kestrio.

Visuals: glass of water (or symbolic) and sticks (powder) just like benchmark brand aquelle.

Design Elements
Use colours that are inside the Vito-Prime Logo, attached.
Product will be available in 3 flavours. Lemon=yellow, Orange=orange, Black Currant=purple

Typography: Utilize strong, clean, and modern fonts. Ensure readability and create a sense of strength, endurance and reliability.

The product will be available in 3 flavours: Lemon, Orange and Johannisbeere

We look forward to seeing your creative ideas and innovative designs for our Vito Prime brand packaging.

```html
<!DOCTYPE html>
<html lang="en">
<head>
<meta charset="utf-8">
<title>Vito Prime Hydration Booster – Flavour Range</title>
<link href="https://fonts.googleapis.com/css2?family=Montserrat:wght@600;700;800&family=Oswald:wght@400;500&display=swap" rel="stylesheet">
<style>
  :root{
    --bg:#e2e2e2;
    --brand-blue:#2342a0;
    --brand-yellow:#eef20a;
    --brand-pink:#d4145f;
    --white:#ffffff;
    --band-yellow:#f6e600;
  }
  *{box-sizing:border-box;margin:0;padding:0}
  html,body{width:1200px;height:720px;overflow:hidden;background:var(--bg)}
  body{font-family:"Montserrat",Arial,sans-serif;position:relative}

  .range{position:absolute;left:30px;top:60px;display:flex;gap:30px}

  .pouch{position:relative;width:360px;height:600px;overflow:hidden;border-radius:6px 6px 10px 10px;color:var(--white)}
  .pouch--currant{--flavour:#9d2592;--flavour-dark:#4a1657;--accent:#4b1552;--band:#e0148c;--badge:#7a1670}
  .pouch--lemon{--flavour:#72cb3c;--flavour-dark:#0b6a33;--accent:#0b6a33;--band:var(--band-yellow);--badge:#0b6a33}
  .pouch--orange{--flavour:#f7a224;--flavour-dark:#ea4320;--accent:#e2401b;--band:var(--band-yellow);--badge:#e2401b}

  .pouch__art{position:absolute;inset:0}

  .seal-line{position:absolute;left:8px;right:8px;top:36px;border-top:1px dashed #111a44}

  .brand{position:absolute;left:0;right:0;top:64px;text-align:center}
  .brand__name{display:inline-flex;align-items:center;gap:10px;font-weight:800;font-size:40px;letter-spacing:-1px;color:var(--brand-yellow);line-height:1}
  .brand__dot{width:26px;height:26px;border-radius:50%;background:var(--brand-pink)}
  .brand__since{display:block;margin:6px 60px 0 0;text-align:right;font-size:11px;font-weight:600;color:var(--white)}

  .pack-info{position:absolute;right:100px;top:166px;text-align:right;font-family:"Oswald",Arial,sans-serif;line-height:1.15}
  .pack-info__count{font-size:15px;font-weight:500}
  .pack-info__weight{font-size:11px}
  .pack-icon{position:absolute;right:70px;top:146px;width:26px;height:62px}

  .stick-badge{position:absolute;right:12px;top:134px;width:52px;height:78px;background:var(--badge);border-radius:2px;text-align:center}
  .stick-badge__num{display:block;font-family:"Oswald",Arial,sans-serif;font-weight:500;font-size:38px;line-height:48px}
  .stick-badge__label{display:block;font-size:9px;font-weight:700;letter-spacing:.3px}

  .headline{position:absolute;left:20px;top:238px;font-weight:800;font-size:28px;letter-spacing:-.6px;white-space:nowrap}
  .tagline{position:absolute;left:20px;top:282px;font-weight:700;font-size:13.5px;letter-spacing:-.2px}
  .descriptor{position:absolute;left:20px;top:314px;font-weight:800;font-size:14.5px;letter-spacing:-.4px;color:var(--accent);white-space:nowrap}

  .benefits{position:absolute;left:20px;top:350px;width:212px;height:116px;border:2px solid var(--accent);border-radius:12px;color:var(--accent);font-family:"Oswald",Arial,sans-serif;display:grid;grid-template-columns:1fr 1fr;grid-template-rows:1fr 1fr;padding:10px 8px}
  .benefit{display:flex;align-items:center;gap:6px;font-size:11.5px;line-height:1.1;text-transform:uppercase}
  .benefit__big{font-family:"Montserrat",Arial,sans-serif;font-weight:800;font-size:24px}
  .benefit svg{flex:none}

  .fruit{position:absolute;right:10px;top:354px;width:120px;height:120px;border-radius:50%}
  .pouch--currant .fruit{background:radial-gradient(circle at 40% 40%,#4a4458,#141018 70%)}
  .pouch--lemon .fruit{background:radial-gradient(circle at 40% 40%,#fff7a0,#f0d818 70%)}
  .pouch--orange .fruit{background:radial-gradient(circle at 40% 40%,#ffc46a,#f28a12 70%)}

  .flavour-name{position:absolute;right:16px;top:492px;font-weight:800;font-size:13px;color:var(--accent);letter-spacing:.3px}

  .footer{position:absolute;left:0;right:0;bottom:0;height:64px;background:var(--flavour-dark);display:flex;justify-content:space-between;align-items:center;padding:0 18px;font-family:"Oswald",Arial,sans-serif;font-size:13px}
</style>
</head>
<body>
<main class="range">

  <!-- Black Currant -->
  <section class="pouch pouch--currant">
    <svg class="pouch__art" viewBox="0 0 360 600" preserveAspectRatio="none" aria-hidden="true">
      <rect width="360" height="600" fill="var(--flavour)"/>
      <polygon points="0,0 360,0 360,138 0,232" fill="var(--brand-blue)"/>
      <path d="M0,520 L250,520 Q268,520 278,500 L290,484 L360,484 L360,536 L0,536 Z" fill="var(--band)"/>
    </svg>
    <div class="seal-line"></div>
    <div class="brand"><span class="brand__name"><span class="brand__dot"></span>Vito Prime</span><span class="brand__since">Since 1992</span></div>
    <div class="pack-info"><div class="pack-info__count">20g x 20</div><div class="pack-info__weight">NET WT 0.7oz / 20g</div></div>
    <svg class="pack-icon" viewBox="0 0 26 62" aria-hidden="true"><path d="M12 18 L24 4" stroke="#fff" stroke-width="5" stroke-linecap="round"/><path d="M3 34 H23 L21 60 H5 Z" fill="none" stroke="#fff" stroke-width="2"/><path d="M4 42 H22 L21 60 H5 Z" fill="#fff"/></svg>
    <div class="stick-badge"><span class="stick-badge__num">20</span><span class="stick-badge__label">STICKS</span></div>
    <h2 class="headline">HYDRATION BOOSTER</h2>
    <p class="tagline">REFRESH, REPLENISH &amp; RECHARGE!</p>
    <p class="descriptor">PREMIUM ISOTONIC ELECTROLYTE DRINK</p>
    <div class="benefits">
      <div class="benefit"><span class="benefit__big">5X</span>Electrolytes</div>
      <div class="benefit"><svg width="20" height="26" viewBox="0 0 20 26"><rect x="2" y="1" width="9" height="13" rx="4.5" fill="none" stroke="currentColor" stroke-width="1.6"/><rect x="2" y="13" width="9" height="12" rx="4.5" fill="none" stroke="currentColor" stroke-width="1.6"/><circle cx="16" cy="10" r="2.2" fill="none" stroke="currentColor" stroke-width="1.4"/></svg>Vitamins<br>&amp; Minerals</div>
      <div class="benefit"><svg width="18" height="28" viewBox="0 0 18 28"><path d="M11 0 L2 16 H8 L5 28 L16 10 H10 Z" fill="currentColor"/></svg>Fast<br>Hydration</div>
      <div class="benefit"><svg width="24" height="24" viewBox="0 0 24 24"><path d="M2 22 C8 16 6 8 22 2 M4 22 C18 18 12 8 22 4" fill="none" stroke="currentColor" stroke-width="1.6"/></svg>Non GMO</div>
    </div>
    <div class="fruit" role="img" aria-label="Black currant berries with leaves"></div>
    <span class="flavour-name">BLACK CURRANT</span>
    <footer class="footer"><span>NET WT 14.1oz / 400g</span><span>NUTRITIONAL EXPERTISE SINCE 1992</span></footer>
  </section>

  <!-- Lemon -->
  <section class="pouch pouch--lemon">
    <svg class="pouch__art" viewBox="0 0 360 600" preserveAspectRatio="none" aria-hidden="true">
      <rect width="360" height="600" fill="var(--flavour)"/>
      <polygon points="0,0 360,0 360,138 0,232" fill="var(--brand-blue)"/>
      <path d="M0,520 L250,520 Q268,520 278,500 L290,484 L360,484 L360,536 L0,536 Z" fill="var(--band)"/>
    </svg>
    <div class="seal-line"></div>
    <div class="brand"><span class="brand__name"><span class="brand__dot"></span>Vito Prime</span><span class="brand__since">Since 1992</span></div>
    <div class="pack-info"><div class="pack-info__count">20g x 20</div><div class="pack-info__weight">NET WT 0.7oz / 20g</div></div>
    <svg class="pack-icon" viewBox="0 0 26 62" aria-hidden="true"><path d="M12 18 L24 4" stroke="#fff" stroke-width="5" stroke-linecap="round"/><path d="M3 34 H23 L21 60 H5 Z" fill="none" stroke="#fff" stroke-width="2"/><path d="M4 42 H22 L21 60 H5 Z" fill="#fff"/></svg>
    <div class="stick-badge"><span class="stick-badge__num">20</span><span class="stick-badge__label">STICKS</span></div>
    <h2 class="headline">HYDRATION BOOSTER</h2>
    <p class="tagline">REFRESH, REPLENISH &amp; RECHARGE!</p>
    <p class="descriptor">PREMIUM ISOTONIC ELECTROLYTE DRINK</p>
    <div class="benefits">
      <div class="benefit"><span class="benefit__big">5X</span>Electrolytes</div>
      <div class="benefit"><svg width="20" height="26" viewBox="0 0 20 26"><rect x="2" y="1" width="9" height="13" rx="4.5" fill="none" stroke="currentColor" stroke-width="1.6"/><rect x="2" y="13" width="9" height="12" rx="4.5" fill="none" stroke="currentColor" stroke-width="1.6"/><circle cx="16" cy="10" r="2.2" fill="none" stroke="currentColor" stroke-width="1.4"/></svg>Vitamins<br>&amp; Minerals</div>
      <div class="benefit"><svg width="18" height="28" viewBox="0 0 18 28"><path d="M11 0 L2 16 H8 L5 28 L16 10 H10 Z" fill="currentColor"/></svg>Fast<br>Hydration</div>
      <div class="benefit"><svg width="24" height="24" viewBox="0 0 24 24"><path d="M2 22 C8 16 6 8 22 2 M4 22 C18 18 12 8 22 4" fill="none" stroke="currentColor" stroke-width="1.6"/></svg>Non GMO</div>
    </div>
    <div class="fruit" role="img" aria-label="Whole and halved lemons with leaves"></div>
    <span class="flavour-name">LEMON</span>
    <footer class="footer"><span>NET WT 14.1oz / 400g</span><span>NUTRITIONAL EXPERTISE SINCE 1992</span></footer>
  </section>

  <!-- Orange -->
  <section class="pouch pouch--orange">
    <svg class="pouch__art" viewBox="0 0 360 600" preserveAspectRatio="none" aria-hidden="true">
      <rect width="360" height="600" fill="var(--flavour)"/>
      <polygon points="0,0 360,0 360,138 0,232" fill="var(--brand-blue)"/>
      <path d="M0,520 L250,520 Q268,520 278,500 L290,484 L360,484 L360,536 L0,536 Z" fill="var(--band)"/>
    </svg>
    <div class="seal-line"></div>
    <div class="brand"><span class="brand__name"><span class="brand__dot"></span>Vito Prime</span><span class="brand__since">Since 1992</span></div>
    <div class="pack-info"><div class="pack-info__count">20g x 20</div><div class="pack-info__weight">NET WT 0.7oz / 20g</div></div>
    <svg class="pack-icon" viewBox="0 0 26 62" aria-hidden="true"><path d="M12 18 L24 4" stroke="#fff" stroke-width="5" stroke-linecap="round"/><path d="M3 34 H23 L21 60 H5 Z" fill="none" stroke="#fff" stroke-width="2"/><path d="M4 42 H22 L21 60 H5 Z" fill="#fff"/></svg>
    <div class="stick-badge"><span class="stick-badge__num">20</span><span class="stick-badge__label">STICKS</span></div>
    <h2 class="headline">HYDRATION BOOSTER</h2>
    <p class="tagline">REFRESH, REPLENISH &amp; RECHARGE!</p>
    <p class="descriptor">PREMIUM ISOTONIC ELECTROLYTE DRINK</p>
    <div class="benefits">
      <div class="benefit"><span class="benefit__big">5X</span>Electrolytes</div>
      <div class="benefit"><svg width="20" height="26" viewBox="0 0 20 26"><rect x="2" y="1" width="9" height="13" rx="4.5" fill="none" stroke="currentColor" stroke-width="1.6"/><rect x="2" y="13" width="9" height="12" rx="4.5" fill="none" stroke="currentColor" stroke-width="1.6"/><circle cx="16" cy="10" r="2.2" fill="none" stroke="currentColor" stroke-width="1.4"/></svg>Vitamins<br>&amp; Minerals</div>
      <div class="benefit"><svg width="18" height="28" viewBox="0 0 18 28"><path d="M11 0 L2 16 H8 L5 28 L16 10 H10 Z" fill="currentColor"/></svg>Fast<br>Hydration</div>
      <div class="benefit"><svg width="24" height="24" viewBox="0 0 24 24"><path d="M2 22 C8 16 6 8 22 2 M4 22 C18 18 12 8 22 4" fill="none" stroke="currentColor" stroke-width="1.6"/></svg>Non GMO</div>
    </div>
    <div class="fruit" role="img" aria-label="Whole and halved oranges with leaves"></div>
    <span class="flavour-name">ORANGE</span>
    <footer class="footer"><span>NET WT 14.1oz / 400g</span><span>NUTRITIONAL EXPERTISE SINCE 1992</span></footer>
  </section>

</main>
</body>
</html>
```